Soft furnishing company selling fabrics, curtains, bedlinen craft & haberdashery

We need 4 x home page banners for our website as follows:
Image 1 - to lead customers to our "New season Fabrics" page,
Image 2 - to lead customers to our Ready Made curtains,
Image 3 - to lead customers to our "Polar Bear Bed linen" page
Image 4 - to lead customers to our "Christmas raft Tutorial" page

Banner needs to be 960px wide x 380px 72dpi and optimised for web. should have a little descriptive text for example "Fabulous Fabric. Prints, plains & weaves, view our range of new season furnishing fabrics to buy by the metre" "Instantly update your home with our range of ready made curtains. Available . "Cosy Night In. Snuggle with this Polar Bear Duvet Set. From €20" "" "Let's Get Crafting for Christmas. Download our free Project and tutoirals here. First 3 images need a "shop now" button

website url www.lintelway.ie

Target Market(s)

Female 25 -45

Industry/Entity Type

It Company

Font styles to use
Serif
Sans Serif

Requirements
Must have
• shop now button on image 1, 2, 3
Should not have
• too much text or clutter

```html
<!DOCTYPE html>
<html lang="en">
<head>
<meta charset="utf-8">
<title>Ready Made Curtains – Instant Update</title>
<link rel="stylesheet" href="https://fonts.googleapis.com/css2?family=Lato:wght@300;400&display=swap">
<style>
  :root {
    --wall-dark: #2f3036;
    --wing-leather: #8c6a3a;
    --chair-plaid: #6d4a48;
    --curtain-grey: #5b5b66;
    --curtain-red: #8b3a35;
    --window-light: #d8d2bf;
    --floor-amber: #b5753e;
    --crate-beige: #b9a58a;
    --panel-veil: rgba(246, 242, 236, 0.76);
    --ink: #2a2626;
    --button-red: #7b0c0f;
    --button-text: #ffffff;
  }
  * { margin: 0; padding: 0; box-sizing: border-box; }
  html, body {
    width: 1200px;
    height: 475px;
    overflow: hidden;
    background: #ffffff;
  }
  .banner {
    position: relative;
    width: 1200px;
    height: 475px;
    overflow: hidden;
    font-family: "Lato", "Helvetica Neue", Arial, sans-serif;
  }
  .banner__scene {
    position: absolute;
    inset: 0;
    width: 100%;
    height: 100%;
  }
  .promo-panel {
    position: absolute;
    left: 700px;
    top: 198px;
    width: 500px;
    height: 233px;
    background: var(--panel-veil);
    text-align: center;
    color: var(--ink);
  }
  .promo-panel__title {
    position: absolute;
    left: 0;
    right: 0;
    top: 22px;
    font-weight: 300;
    font-size: 56px;
    line-height: 1;
    letter-spacing: -0.5px;
    text-transform: uppercase;
  }
  .promo-panel__text {
    position: absolute;
    left: 0;
    right: 0;
    top: 85px;
    font-weight: 400;
    font-size: 24.5px;
    line-height: 31px;
  }
  .promo-panel__button {
    position: absolute;
    left: 150px;
    top: 162px;
    width: 165px;
    height: 42px;
    background: var(--button-red);
    color: var(--button-text);
    font-size: 25px;
    line-height: 42px;
    text-decoration: none;
  }
</style>
</head>
<body>
  <section class="banner">
    <svg class="banner__scene" viewBox="0 0 1200 475" preserveAspectRatio="none"
         role="img" aria-label="Living room with a tan leather wingback armchair and tartan cushion beside full-length red and grey tartan ready made curtains framing a bright window, a glass decanter on stacked books and a warm wooden floor">
      <defs>
        <linearGradient id="roomTones" x1="0" y1="0" x2="1" y2="0">
          <stop offset="0" stop-color="var(--wing-leather)"/>
          <stop offset="0.16" stop-color="var(--chair-plaid)"/>
          <stop offset="0.24" stop-color="var(--wall-dark)"/>
          <stop offset="0.3" stop-color="var(--curtain-grey)"/>
          <stop offset="0.4" stop-color="var(--curtain-red)"/>
          <stop offset="0.49" stop-color="var(--curtain-grey)"/>
          <stop offset="0.53" stop-color="var(--window-light)"/>
          <stop offset="0.56" stop-color="var(--curtain-grey)"/>
          <stop offset="0.68" stop-color="var(--curtain-red)"/>
          <stop offset="0.8" stop-color="var(--curtain-grey)"/>
          <stop offset="0.88" stop-color="var(--curtain-red)"/>
          <stop offset="0.93" stop-color="var(--wall-dark)"/>
          <stop offset="1" stop-color="var(--crate-beige)"/>
        </linearGradient>
        <linearGradient id="floorGlow" x1="0" y1="0" x2="0" y2="1">
          <stop offset="0.72" stop-color="var(--floor-amber)" stop-opacity="0"/>
          <stop offset="1" stop-color="var(--floor-amber)" stop-opacity="0.6"/>
        </linearGradient>
      </defs>
      <rect width="1200" height="475" fill="url(#roomTones)"/>
      <rect width="1200" height="475" fill="url(#floorGlow)"/>
    </svg>

    <div class="promo-panel">
      <h1 class="promo-panel__title">Instant Update</h1>
      <p class="promo-panel__text">Revive your home with our<br>range of ready made curtains</p>
      <a class="promo-panel__button" href="#">Shop Now</a>
    </div>
  </section>
</body>
</html>
```